Business Card for Bright Meadow Lawn & Landscape

Double Sided Card Design - I think one side of the card should be cleaner, with logo, contact info, and "Complete Residential & Commercial Landscape Services", and on the other side it should list the services we offer:

- Lawn Care & Mowing
- Hedge & Shrub Trimming
- Leaf Removal & Clean Up
- Aeration & Sod
- Mulch & Rock Installations
- Landscape Installations & Renovations
- Commercial Snow Removal

Please make it clean and very professional... don't want it too be too busy, but want to tell them what we do.

Target Market(s)

Residential and Commercial

Industry/Entity Type

Landscape

Contact Information for Business Card

Fully Insured
Tom Berrigan
410-555-0198
Tberrigan07@mailbox-example.com

Requirements
Must have
• Double Sided, Cleaner on one side, more information and text on the other side.

```html
<!DOCTYPE html>
<html lang="en">
<head>
<meta charset="utf-8">
<title>Bright Meadow Lawn &amp; Landscape – Business Card</title>
<link href="https://fonts.googleapis.com/css2?family=Cinzel:wght@600&family=Tinos:ital@0;1&display=swap" rel="stylesheet">
<style>
  :root {
    --stage: #2b2b2b;
    --card: #0b0b0b;
    --card-edge: #161616;
    --green: #7dbb42;
    --white: #f4f4f4;
  }
  * { box-sizing: border-box; margin: 0; padding: 0; }
  html, body { width: 1200px; height: 1200px; overflow: hidden; }
  body {
    background: var(--stage);
    font-family: "Tinos", "Times New Roman", serif;
    color: var(--white);
    position: relative;
  }
  .card {
    position: absolute;
    left: 150px;
    width: 900px;
    height: 514px;
    background: linear-gradient(160deg, var(--card-edge), var(--card) 55%);
    box-shadow: 0 14px 30px rgba(0,0,0,.55);
  }
  .card--services { top: 66px; }
  .card--contact { top: 620px; }

  .divider {
    position: absolute;
    width: 2px;
    background: var(--green);
  }

  /* services side */
  .services-mark {
    position: absolute;
    left: 110px;
    top: 150px;
    width: 260px;
    display: flex;
    flex-direction: column;
    align-items: center;
    gap: 18px;
  }
  .mark-circle {
    width: 130px; height: 130px;
    border: 14px solid var(--green);
    border-radius: 50%;
  }
  .mark-name {
    font-family: "Cinzel", serif;
    font-weight: 600;
    color: var(--green);
    font-size: 26px;
    letter-spacing: 1px;
    text-align: center;
  }
  .card--services .divider { left: 440px; top: 125px; height: 260px; }
  .service-list {
    position: absolute;
    left: 480px;
    top: 135px;
    list-style: none;
    font-size: 23px;
    line-height: 34px;
  }

  /* contact side */
  .brand {
    position: absolute;
    left: 60px;
    top: 70px;
    width: 380px;
    display: flex;
    flex-direction: column;
    align-items: center;
  }
  .brand .mark-circle { width: 150px; height: 150px; border-width: 16px; margin-bottom: 22px; }
  .brand-name {
    font-family: "Cinzel", serif;
    font-weight: 600;
    color: var(--green);
    text-align: center;
    line-height: 1.15;
  }
  .brand-name .line1 { display: block; font-size: 42px; }
  .brand-name .line2 { display: block; font-size: 22px; letter-spacing: 6px; }
  .card--contact .divider { left: 470px; top: 90px; height: 230px; }
  .contact {
    position: absolute;
    left: 505px;
    top: 130px;
  }
  .person {
    font-family: "Cinzel", serif;
    font-weight: 600;
    font-size: 34px;
    letter-spacing: 1px;
    margin-bottom: 16px;
  }
  .person .first { color: var(--green); }
  .contact-row {
    display: flex;
    align-items: center;
    gap: 10px;
    font-size: 21px;
    margin-bottom: 10px;
  }
  .contact-row svg { flex: none; }
  .tagline-rule {
    position: absolute;
    left: 60px; right: 60px;
    top: 420px;
    height: 2px;
    background: var(--green);
  }
  .tagline {
    position: absolute;
    left: 0; right: 0;
    top: 376px;
    text-align: center;
    font-style: italic;
    font-size: 28px;
  }
  .insured {
    position: absolute;
    left: 50%;
    top: 407px;
    transform: translateX(-50%);
    padding: 0 14px;
    background: var(--card);
    color: var(--green);
    font-style: italic;
    font-size: 24px;
  }
</style>
</head>
<body>

<section class="card card--services">
  <div class="services-mark">
    <div class="mark-circle"></div>
    <div class="mark-name">Bright Meadow</div>
  </div>
  <div class="divider"></div>
  <ul class="service-list">
    <li>Lawn Care &amp; Mowing</li>
    <li>Hedge &amp; Shrub Trimming</li>
    <li>Leaf Removal &amp; Clean Up</li>
    <li>Aeration &amp; Sod</li>
    <li>Mulch &amp; Rock Installations</li>
    <li>Landscape Installations &amp; Renovations</li>
    <li>Commercial Snow Removal</li>
  </ul>
</section>

<section class="card card--contact">
  <div class="brand">
    <div class="mark-circle"></div>
    <div class="brand-name">
      <span class="line1">Bright Meadow</span>
      <span class="line2">Lawn &amp; Landscape</span>
    </div>
  </div>
  <div class="divider"></div>
  <div class="contact">
    <div class="person"><span class="first">Tom</span> Berrigan</div>
    <div class="contact-row">
      <svg width="26" height="26" viewBox="0 0 26 26" aria-hidden="true">
        <circle cx="13" cy="13" r="11.5" fill="none" stroke="#7dbb42" stroke-width="2"/>
        <path d="M8 9.5c0-1 1-1.8 2-1.5l1 2.2-1.2 1.2c.7 1.6 1.9 2.8 3.5 3.5l1.2-1.2 2.2 1c.3 1-.5 2-1.5 2C10.8 16.7 8 13.9 8 9.5z" fill="#7dbb42"/>
      </svg>
      <span>410-555-0198</span>
    </div>
    <div class="contact-row">
      <svg width="26" height="26" viewBox="0 0 26 26" aria-hidden="true">
        <circle cx="13" cy="13" r="11.5" fill="none" stroke="#7dbb42" stroke-width="2"/>
        <rect x="7" y="9" width="12" height="8" fill="none" stroke="#7dbb42" stroke-width="1.6"/>
        <path d="M7 9l6 5 6-5" fill="none" stroke="#7dbb42" stroke-width="1.6"/>
      </svg>
      <span>Tberrigan07@mailbox-example.com</span>
    </div>
  </div>
  <p class="tagline">Complete Residential &amp; Commercial Landscape Services</p>
  <div class="tagline-rule"></div>
  <span class="insured">Fully Insured</span>
</section>

</body>
</html>
```